Velvor IT Services Business Card

Velvor IT Services are a Perth based IT Services company. We would like to incorporate our company logo (attached) and stick with the blue that is in that design. I would like a clean look design that isn't too busy, yet creates a lasting image that is instantly recognisable in the recipients mind.

Target Market(s)

The target audience is small/medium business owners.

Industry/Entity Type

Business

Font styles to use
Serif
Sans Serif

Colors

Designer to choose colors to be used in the design.

Requirements
Must have
• The design should include:
Business name: Velvor IT Services
Directors Name: Marcus Dredge
Phone Number: 0483 906 452
Email: support@velvorit.com.au
Website: www.velvorit.com.au

```html
<!DOCTYPE html>
<html lang="en">
<head>
<meta charset="utf-8">
<title>Velvor IT Services – Business Card</title>
<link rel="stylesheet" href="https://fonts.googleapis.com/css2?family=Mulish:wght@400;700;800&display=swap">
<style>
  :root {
    --page-bg: #e9ebee;
    --card-white: #ffffff;
    --card-black: #0b0b0c;
    --brand-blue: #1b8fe0;
    --brand-blue-light: #35b8f0;
    --brand-blue-deep: #1560c8;
    --text-light: #e6e6e6;
    --text-white: #ffffff;
  }
  * { box-sizing: border-box; margin: 0; padding: 0; }
  html, body {
    width: 1200px; height: 900px; overflow: hidden;
    background: var(--page-bg);
    font-family: "Mulish", "Helvetica Neue", Arial, sans-serif;
  }
  .sheet {
    width: 1200px; height: 900px;
    display: flex; align-items: center; justify-content: center; gap: 48px;
  }
  .card {
    position: relative;
    width: 520px; height: 318px;
    border-radius: 4px;
    overflow: hidden;
    box-shadow: 0 10px 30px rgba(0,0,0,0.18);
  }

  /* Front */
  .card--front {
    background: var(--card-white);
    display: flex; align-items: center; justify-content: center;
  }
  .brand {
    display: flex; align-items: center; gap: 14px;
  }
  .brand__mark {
    width: 34px; height: 34px;
    background: var(--brand-blue);
  }
  .brand__name {
    font-size: 30px; font-weight: 800;
    color: var(--brand-blue-deep);
    letter-spacing: 0.5px;
  }

  /* Back */
  .card--back { background: var(--card-black); }
  .back__mark {
    position: absolute; left: 34px; top: 40px;
    width: 120px; height: 120px;
    background: linear-gradient(135deg, var(--brand-blue-light), var(--brand-blue-deep));
  }
  .name-band {
    position: absolute; left: 262px; right: 0; top: 108px;
    height: 44px;
    background: var(--brand-blue);
    display: flex; align-items: center;
    padding-left: 18px;
  }
  .name-band__name {
    color: var(--text-white);
    font-size: 22px; font-weight: 700;
  }
  .contact-list {
    position: absolute; left: 232px; top: 172px;
    list-style: none;
  }
  .contact-list__item {
    display: flex; align-items: baseline;
    font-size: 15px; color: var(--text-light);
    line-height: 27px;
    letter-spacing: 0.4px;
  }
  .contact-list__label {
    width: 30px;
    color: var(--brand-blue);
    font-weight: 700; font-size: 12px;
  }
</style>
</head>
<body>
  <main class="sheet">
    <section class="card card--front" aria-label="Card front">
      <div class="brand">
        <span class="brand__mark"></span>
        <span class="brand__name">Velvor IT Services</span>
      </div>
    </section>

    <section class="card card--back" aria-label="Card back">
      <div class="back__mark"></div>
      <div class="name-band">
        <span class="name-band__name">Marcus Dredge</span>
      </div>
      <ul class="contact-list">
        <li class="contact-list__item"><span class="contact-list__label">P</span>0483 906 452</li>
        <li class="contact-list__item"><span class="contact-list__label">E</span>support@velvorit.com.au</li>
        <li class="contact-list__item"><span class="contact-list__label">W</span>www.velvorit.com.au</li>
      </ul>
    </section>
  </main>
</body>
</html>
```